Business Card Re-Design for a Lighting Designer

I would like my business card re-designed. It is currently high gloss and they scratch too easily. I don not think the current design lends itself well to a matte finish. I have included the current design for reference along with our company logo.
Check out our website for current branding.
http://www.brambleorchidstudio.example

Updates
Some of the top contenders are muslim and it is a holiday for them. I do not want to discriminate and would expect the same courtesy for holidays we celebrate.
Target Market(s)
Interior Designers, Architects
Contact Information for Business Card
Logo - Name, Title, Address, Telephone Number and Extension, Email
Font styles to use
Requirements
Must have
- All the information listed on the current business card. If you use Red, it needs to be the red from our logo.
Nice to have
- Vertical and Horizontal Designs will be entertained.
Should not have
- Requirements for a glossy finish...should not look too corporate since we are a design firm.

```html
<!DOCTYPE html>
<html lang="en">
<head>
<meta charset="utf-8">
<title>Bramble Orchid Studio – Business Card</title>
<link rel="stylesheet" href="https://fonts.googleapis.com/css2?family=Roboto:wght@300;400;500;700&display=swap">
<style>
  :root {
    --brand-red: #9e1b20;
    --brand-red-light: #b0282d;
    --ink: #1d1d1d;
    --text-grey: #555555;
    --rule-grey: #9a9a9a;
    --accent-salmon: #d9957d;
    --paper: #ffffff;
    --backdrop: #2a2a2a;
  }
  * { margin: 0; padding: 0; box-sizing: border-box; }
  html, body { width: 1200px; height: 895px; overflow: hidden; }
  body {
    background: var(--backdrop);
    font-family: "Roboto", Arial, sans-serif;
    position: relative;
  }
  .card {
    position: absolute;
    width: 560px;
    height: 320px;
    overflow: hidden;
    box-shadow: 0 12px 30px rgba(0,0,0,0.45);
  }

  /* Back of card */
  .card-back {
    left: 80px;
    top: 90px;
    background: var(--brand-red);
  }
  .card-back .pattern-field {
    position: absolute;
    right: 0; top: 0;
    width: 62%;
    height: 100%;
    background: linear-gradient(135deg, var(--brand-red-light) 0%, var(--brand-red) 75%);
  }
  .card-back .brand-lockup {
    position: absolute;
    left: 50%; top: 50%;
    transform: translate(-50%, -50%);
    display: flex;
    align-items: center;
    gap: 18px;
  }
  .brand-square {
    width: 26px; height: 26px;
    flex: none;
  }
  .card-back .brand-square { background: var(--paper); }
  .card-back .brand-name {
    color: var(--paper);
    font-weight: 300;
    font-size: 30px;
    letter-spacing: 1px;
    text-transform: uppercase;
    white-space: nowrap;
  }

  /* Front of card */
  .card-front {
    left: 560px;
    top: 470px;
    background: var(--paper);
  }
  .card-front .brand-lockup {
    position: absolute;
    right: 28px;
    top: 40px;
    display: flex;
    align-items: center;
    gap: 12px;
  }
  .card-front .brand-square { background: var(--brand-red); width: 22px; height: 22px; }
  .card-front .brand-name {
    color: var(--ink);
    font-weight: 300;
    font-size: 24px;
    letter-spacing: 0.5px;
    text-transform: uppercase;
    white-space: nowrap;
  }
  .card-front .header-rule {
    position: absolute;
    left: 30px;
    right: 28px;
    top: 130px;
    height: 1px;
    background: var(--rule-grey);
  }
  .person {
    position: absolute;
    left: 30px;
    top: 150px;
  }
  .person-name {
    color: var(--brand-red);
    font-weight: 700;
    font-size: 21px;
    letter-spacing: 0.3px;
    text-transform: uppercase;
  }
  .person-title {
    color: var(--text-grey);
    font-size: 14px;
    margin-top: 2px;
  }
  .person .name-rule {
    width: 220px;
    height: 1px;
    background: var(--rule-grey);
    margin-top: 10px;
  }
  .contact-list {
    position: absolute;
    left: 30px;
    top: 218px;
    list-style: none;
  }
  .contact-list li {
    display: flex;
    align-items: center;
    gap: 10px;
    font-size: 13px;
    color: var(--ink);
    height: 19px;
  }
  .contact-list svg { width: 12px; height: 12px; fill: var(--brand-red); flex: none; }
  .footer-band {
    position: absolute;
    left: 0; right: 0; bottom: 0;
    height: 6px;
    display: flex;
  }
  .footer-band .band-salmon { flex: 3; background: var(--accent-salmon); height: 3px; align-self: flex-end; }
  .footer-band .band-red { flex: 1.3; background: var(--brand-red); }
</style>
</head>
<body>

  <section class="card card-back" aria-label="Card back">
    <div class="pattern-field" role="img" aria-label="Faint tonal red geometric cell pattern"></div>
    <div class="brand-lockup">
      <span class="brand-square"></span>
      <span class="brand-name">Bramble Orchid Studio</span>
    </div>
  </section>

  <section class="card card-front" aria-label="Card front">
    <div class="brand-lockup">
      <span class="brand-square"></span>
      <span class="brand-name">Bramble Orchid Studio</span>
    </div>
    <div class="header-rule"></div>

    <div class="person">
      <div class="person-name">Daniel Harwood</div>
      <div class="person-title">Managing Director</div>
      <div class="name-rule"></div>
    </div>

    <ul class="contact-list">
      <li>
        <svg viewBox="0 0 24 24" aria-hidden="true"><path d="M6.6 10.8a15.1 15.1 0 0 0 6.6 6.6l2.2-2.2a1 1 0 0 1 1-.25 11.4 11.4 0 0 0 3.6.57 1 1 0 0 1 1 1V20a1 1 0 0 1-1 1A17 17 0 0 1 3 4a1 1 0 0 1 1-1h3.5a1 1 0 0 1 1 1c0 1.25.2 2.45.57 3.57a1 1 0 0 1-.25 1z"/></svg>
        000 000 0000
      </li>
      <li>
        <svg viewBox="0 0 24 24" aria-hidden="true"><path d="M6 2h12v5H6zM4 8h16a2 2 0 0 1 2 2v7h-4v5H6v-5H2v-7a2 2 0 0 1 2-2zm4 9v3h8v-3z"/></svg>
        000 000 0000
      </li>
      <li>
        <svg viewBox="0 0 24 24" aria-hidden="true"><path d="M2 5h20v14H2zm2 2v.5l8 5 8-5V7l-8 5z"/></svg>
        info@brambleorchidstudio.example
      </li>
      <li>
        <svg viewBox="0 0 24 24" aria-hidden="true"><path d="M12 2a10 10 0 1 0 0 20 10 10 0 0 0 0-20zm0 2c.9 1.2 1.6 2.8 1.9 5h-3.8c.3-2.2 1-3.8 1.9-5zM4.3 11h3.8c0-.7.1-1.4.2-2H5a8 8 0 0 0-.7 2zm0 2a8 8 0 0 0 .7 2h3.3c-.1-.6-.2-1.3-.2-2zm5.8 0c0 .7.1 1.4.2 2h3.4c.1-.6.2-1.3.2-2zm0-2h3.8c0-.7-.1-1.4-.2-2h-3.4c-.1.6-.2 1.3-.2 2zm5.8 0h3.8a8 8 0 0 0-.7-2h-3.3c.1.6.2 1.3.2 2zm0 2c0 .7-.1 1.4-.2 2H19a8 8 0 0 0 .7-2zm-5.8 4c.3 1.3.9 2.3 1.9 3 1-.7 1.6-1.7 1.9-3z"/></svg>
        www.brambleorchidstudio.example
      </li>
    </ul>

    <div class="footer-band">
      <span class="band-salmon"></span>
      <span class="band-red"></span>
    </div>
  </section>

</body>
</html>
```